Service company standing banner design

We are an existing company that just updated our logo. We are attending some oportunity summits in the near future and want a new crisp clean look on our three banners that will be placed in the back of our small booth. The summits we are attending are designed to give local companies opportunities on a prokect we have been awarded to construct in their area. These banners should communicate who we are with no questions when people see them. One banner shall list our services. One to list our values and one to state our goals. All these while being appealing to the eye and using picture of nature. Attached are copies of what we are to replace. also the new logo and the original background pictures in the existing banners

```html
<!DOCTYPE html>
<html lang="en">
<head>
<meta charset="utf-8">
<title>Norvale Services – Booth Banners</title>
<link href="https://fonts.googleapis.com/css2?family=Baloo+2:wght@700;800&family=Nunito:wght@800;900&family=Poppins:wght@500;600&display=swap" rel="stylesheet">
<style>
  :root{
    --navy:#0c1c28;
    --orange:#f47920;
    --orange-light:#f99a4a;
    --blue:#1a4ca0;
    --heading-orange:#f07828;
    --ink:#1d1d1d;
    --white:#ffffff;
  }
  *{margin:0;padding:0;box-sizing:border-box}
  html,body{width:1200px;height:1200px;overflow:hidden}
  body{
    position:relative;
    background:linear-gradient(180deg,#a2bb98 0%,#8fb082 35%,#5f9446 65%,#2f6a22 82%,#0f2a0a 86%,#000 87%,#000 100%);
    font-family:"Poppins",sans-serif;
  }
  .board-title{
    position:absolute;top:28px;left:0;width:100%;text-align:center;
    font-weight:600;font-size:32px;color:var(--heading-orange);
  }
  .deliverables{
    position:absolute;top:94px;left:0;width:100%;text-align:center;
    font-weight:500;font-size:25px;color:var(--ink);
  }
  .deliverables .formats{color:var(--blue)}
  .deliverables .divider{color:var(--blue);margin:0 14px}

  .banner{position:absolute;top:190px;width:358px;height:845px;overflow:hidden;background:var(--navy)}
  .banner--values{left:44px}
  .banner--services{left:427px}
  .banner--goals{left:810px}
  .photo{position:absolute;inset:0}
  .photo--forest-lake{background:linear-gradient(160deg,#2c3a2a 0%,#1f3222 30%,#2f5b58 50%,#3f6c6a 60%,#5a5038 75%,#2a2e22 100%)}
  .photo--snow-forest{background:linear-gradient(180deg,#8fa6c4 0%,#c6d0dc 22%,#e6ebf0 45%,#d4dbe4 65%,#f2f4f7 85%,#ffffff 100%)}
  .photo--mountain-river{background:linear-gradient(180deg,#c9ced2 0%,#5d6a60 14%,#2b3a2a 35%,#1e2e1e 55%,#4a6e70 75%,#7a9a98 88%,#5f7e7e 100%)}
  .shapes{position:absolute;inset:0;width:358px;height:845px}

  .values-list{position:absolute;left:30px;top:214px;list-style:none;
    font-family:"Baloo 2",sans-serif;font-weight:800;font-size:44px;line-height:53px;
    color:var(--blue);text-shadow:2px 0 #fff,-2px 0 #fff,0 2px #fff,0 -2px #fff,2px 2px #fff,-2px -2px #fff,2px -2px #fff,-2px 2px #fff;}
  .values-list .initial{color:var(--orange)}

  .services-title{position:absolute;right:12px;top:74px;
    font-family:"Baloo 2",sans-serif;font-weight:800;font-size:44px;line-height:48px;color:var(--white);
    text-shadow:2px 0 var(--orange),-2px 0 var(--orange),0 2px var(--orange),0 -2px var(--orange),2px 2px var(--orange),-2px -2px var(--orange);}
  .service{position:absolute;right:15px;text-align:right;
    font-family:"Baloo 2",sans-serif;font-weight:800;font-size:25px;line-height:24px;color:var(--blue);
    text-shadow:1.5px 0 #fff,-1.5px 0 #fff,0 1.5px #fff,0 -1.5px #fff,1.5px 1.5px #fff,-1.5px -1.5px #fff;}

  .goal-heading{position:absolute;left:0;top:68px;width:100%;text-align:center;
    font-family:"Nunito",sans-serif;font-weight:900;font-size:40px;line-height:42px;color:var(--white)}
  .goal-statement{position:absolute;left:0;top:270px;width:100%;text-align:center;
    font-family:"Nunito",sans-serif;font-weight:800;font-size:35px;line-height:44px;color:var(--orange)}
  .goal-statement strong{font-weight:900}

  .brand{position:absolute;display:flex;align-items:center;gap:8px}
  .brand-mark{width:40px;height:40px;border-radius:50%;background:var(--orange);flex:none}
  .brand-name{font-family:"Baloo 2",sans-serif;font-weight:700;font-size:22px;line-height:22px;color:var(--blue)}
  .brand-name span{display:block;font-size:17px;line-height:19px}
  .banner--values .brand{left:66px;top:652px}
  .banner--services .brand{left:120px;top:752px}
  .banner--goals .brand{left:68px;top:706px}

  .social{position:absolute;display:flex;gap:3px;list-style:none}
  .social li{width:32px;height:32px;border-radius:5px;background:var(--white)}
  .banner--values .social{left:168px;top:735px}
  .banner--goals .social{left:138px;top:773px}
</style>
</head>
<body>
  <h1 class="board-title">All Banners</h1>
  <p class="deliverables">Deliverables: Ediatable: <span class="formats">AI, PDF, EPS</span><span class="divider">|</span>Output Format: <span class="formats">JPG, PNG, TIFF</span></p>

  <section class="banner banner--values">
    <div class="photo photo--forest-lake" role="img" aria-label="Photo of a pine forest above a turquoise lake"></div>
    <svg class="shapes" viewBox="0 0 448 1057" preserveAspectRatio="none" aria-hidden="true">
      <path d="M0 0 H260 C200 80 150 140 110 200 C80 240 40 245 0 258 Z" fill="var(--navy)"/>
      <path d="M260 0 C210 90 160 130 120 190 C90 230 50 250 0 258 L0 245 C40 235 70 215 95 180 C140 115 200 70 240 0 Z" fill="var(--orange-light)"/>
      <path d="M100 168 C130 120 180 85 215 70 C180 110 150 160 120 200 C110 190 105 180 100 168Z" fill="var(--blue)"/>
      <path d="M0 893 C120 800 200 700 270 580 C320 520 380 500 448 503 V1057 H0 Z" fill="var(--navy)"/>
      <path d="M0 893 C90 820 130 740 180 660 C220 600 270 590 300 580 C250 650 200 720 150 770 C100 820 50 860 0 893 Z" fill="var(--orange)"/>
      <path d="M280 570 C310 520 350 495 390 493 C360 510 330 540 300 580 Z" fill="var(--blue)"/>
    </svg>
    <ul class="values-list">
      <li><span class="initial">I</span>ntegrity</li>
      <li><span class="initial">T</span>ransparency</li>
      <li><span class="initial">R</span>espect</li>
      <li><span class="initial">T</span>rust</li>
    </ul>
    <div class="brand"><i class="brand-mark"></i><p class="brand-name">Norvale Services<span>Limited Partnership</span></p></div>
    <ul class="social" aria-label="Social channels"><li></li><li></li><li></li><li></li></ul>
  </section>

  <section class="banner banner--services">
    <div class="photo photo--snow-forest" role="img" aria-label="Photo of snow-covered spruce trees under a winter sky"></div>
    <svg class="shapes" viewBox="0 0 448 1057" preserveAspectRatio="none" aria-hidden="true">
      <path d="M110 915 L448 850 V1057 H110 Z" fill="var(--navy)"/>
      <path d="M0 0 H80 C110 200 30 350 40 500 C50 650 110 750 60 1057 H0 Z" fill="var(--navy)"/>
      <path d="M80 0 H150 C140 150 170 300 180 450 C190 600 150 750 165 1057 H60 C110 750 50 650 40 500 C30 350 110 200 80 0Z" fill="var(--orange)"/>
      <path d="M100 80 C115 220 60 360 70 500 C80 640 130 760 100 1000 C140 760 120 640 110 500 C100 360 125 220 100 80Z" fill="var(--orange-light)"/>
    </svg>
    <h2 class="services-title">SERVICES</h2>
    <p class="service" style="top:158px">Pipeline<br>Construction</p>
    <p class="service" style="top:226px">Pipeline<br>Clearing</p>
    <p class="service" style="top:297px">Land<br>Clearing</p>
    <p class="service" style="top:370px">Civil<br>Works</p>
    <p class="service" style="top:438px">Road<br>Maintenance</p>
    <p class="service" style="top:508px">Reclamation</p>
    <p class="service" style="top:550px">Logging</p>
    <p class="service" style="top:599px">Mulching</p>
    <div class="brand"><i class="brand-mark"></i><p class="brand-name">Norvale Services<span>Limited Partnership</span></p></div>
  </section>

  <section class="banner banner--goals">
    <div class="photo photo--mountain-river" role="img" aria-label="Photo of forested mountains above a rushing river"></div>
    <svg class="shapes" viewBox="0 0 448 1057" preserveAspectRatio="none" aria-hidden="true">
      <path d="M0 800 C80 770 150 790 220 780 C300 770 360 780 448 790 V1057 H0 Z" fill="var(--orange-light)"/>
      <path d="M0 820 C90 800 160 815 240 800 C320 790 380 815 448 845 V1057 H0 Z" fill="var(--orange)"/>
      <path d="M0 830 C100 850 180 830 260 840 C340 850 400 850 448 855 V1057 H0 Z" fill="var(--navy)"/>
    </svg>
    <h2 class="goal-heading">Honouring<br>the interests<br>of indigenous<br>people</h2>
    <p class="goal-statement">To <strong>BUILD</strong> and<br><strong>GROW</strong> a strong<br>regional business<br>providing the<br><strong>BEST QUALITY</strong><br>for our <strong>PEOPLE</strong><br>and <strong>CLIENTS</strong></p>
    <div class="brand"><i class="brand-mark"></i><p class="brand-name">Norvale Services<span>Limited Partnership</span></p></div>
    <ul class="social" aria-label="Social channels"><li></li><li></li><li></li><li></li></ul>
  </section>
</body>
</html>
```